Book Cover - For Best Selling Diet

Hi
Book cover required for a diet book being marketed to become a best seller
For best quality, image will be 2820 pixels on the shortest side and 4500 pixels on the longest side .
The book name : Bright Morning Plan
By Corinna Plett
( will add in the extra text once we see design - top and bottom subtitle )
I do not want a photo of a person on the book.
PLEASE SEE " THE 9 STEP FRAME" by Ned Galbury as an example of solid style and I also love Quiet Ledger for the font.
Branding Colours:
#F26432
#A4195C
#A7D8CC
Font that runs through our brand is : helvetica neue
This is for a book that will be marketed for #1 bestseller - So please only quality
designs that are designed in a unique style.
Thanks
Target Market(s)
Busy Working Mums, Affluent, 30+ .
Look and feel

```html
<!DOCTYPE html>
<html lang="en">
<head>
<meta charset="utf-8">
<title>Bright Morning Plan — Corinna Plett</title>
<link rel="stylesheet" href="https://fonts.googleapis.com/css2?family=Cinzel:wght@400;500&display=swap">
<style>
  :root {
    --bg-top: #f68c50;
    --bg-mid: #e67a48;
    --bg-low: #c84a3a;
    --bg-bottom: #a91f30;
    --title-fill: #e9f6f6;
    --title-edge: #3a2418;
    --author: #a7d8cc;
    --ornament: rgba(20, 12, 8, 0.82);
  }
  * { margin: 0; padding: 0; box-sizing: border-box; }
  html, body { width: 900px; height: 1200px; overflow: hidden; }
  body { background: var(--bg-bottom); }
  .cover {
    position: relative;
    width: 900px;
    height: 1200px;
    overflow: hidden;
    background: linear-gradient(180deg,
      var(--bg-top) 0%,
      var(--bg-top) 30%,
      var(--bg-mid) 58%,
      var(--bg-low) 80%,
      var(--bg-bottom) 100%);
    font-family: "Cinzel", "Times New Roman", serif;
    text-align: center;
  }
  .title {
    position: absolute;
    left: 0;
    width: 100%;
    color: var(--title-fill);
    text-shadow:
      -1px -1px 0 var(--title-edge),
       1px -1px 0 var(--title-edge),
      -1px  1px 0 var(--title-edge),
       1px  1px 0 var(--title-edge),
       2px  3px 4px rgba(60, 20, 10, 0.45);
    line-height: 1;
    font-weight: 400;
  }
  .title-main   { top: 82px;  font-size: 158px; letter-spacing: 4px; }
  .title-middle { top: 316px; font-size: 98px;  letter-spacing: 3px; }
  .title-last   { top: 466px; font-size: 86px;  letter-spacing: 3px; }
  .ornament {
    position: absolute;
    left: 95px;
    top: 566px;
    width: 710px;
    height: 124px;
    background: radial-gradient(ellipse at 50% 90%, var(--ornament) 0%, rgba(20,12,8,0.35) 22%, rgba(20,12,8,0) 60%);
  }
  .author {
    position: absolute;
    left: 0;
    top: 1064px;
    width: 100%;
    font-size: 66px;
    line-height: 1;
    letter-spacing: 4px;
    color: var(--author);
    font-weight: 400;
  }
</style>
</head>
<body>
  <main class="cover">
    <h1 class="book-title">
      <span class="title title-main">BRIGHT</span>
      <span class="title title-middle">MORNING</span>
      <span class="title title-last">PLAN</span>
    </h1>
    <div class="ornament" role="img" aria-label="Decorative black flourish divider with three stacked rings rising from its centre"></div>
    <p class="author">CORINNA PLETT</p>
  </main>
</body>
</html>
```